Discreet simple classy for adult entertainment

I would like a matte black business card with gold writing for my business. Keeping it simple. Having my following:

Lana frost
Events. Entertainment. Promotions
0491726580

or alternatively could have what i had on my previous card below but i think i prefer the above as again - discretion.

Maybe a nice gold line thru the card or some other very simple design . Or not open to ideas/ can be doublesided if any good ideas with that.

included pics of my old bus card. not sure weather i want a photo on it or not. if i do it wont be the same pic. i kinda wanted a card that was discreet so if it was in someones wallet they wouldn't neccessarily realise it was from a stripper.

Target Market(s)

men

Industry/Entity Type

Business

Contact Information for Business Card

Lana frost
0491726580

Requirements
Nice to have
• i don't know i am really open to anything. im giving my cards to guys so something they can have in their wallet that is discreet preferably.

```html
<!DOCTYPE html>
<html lang="en">
<head>
<meta charset="UTF-8">
<title>Lana Frost — Business Card</title>
<link rel="stylesheet" href="https://fonts.googleapis.com/css2?family=Jost:wght@400;600&display=swap">
<style>
  :root {
    --backdrop: #2a2522;
    --card-black: #111111;
    --gold: #f2c300;
  }
  * { margin: 0; padding: 0; box-sizing: border-box; }
  html, body {
    width: 1200px;
    height: 780px;
    overflow: hidden;
    background: var(--backdrop);
  }
  .canvas {
    width: 1200px;
    height: 780px;
    display: flex;
    align-items: center;
    justify-content: center;
  }
  .business-card {
    position: relative;
    width: 1000px;
    height: 580px;
    background: var(--card-black);
    color: var(--gold);
    font-family: "Jost", "Futura", sans-serif;
  }
  .identity {
    position: absolute;
    left: 0;
    width: 820px;
    top: 210px;
    text-align: center;
  }
  .identity__name {
    font-weight: 600;
    font-size: 70px;
    line-height: 1;
    letter-spacing: 1px;
    text-transform: uppercase;
  }
  .identity__services {
    margin-top: 10px;
    font-weight: 400;
    font-size: 25px;
    letter-spacing: 0.5px;
    text-transform: uppercase;
  }
  .identity__phone {
    margin-top: 4px;
    font-weight: 400;
    font-size: 30px;
    letter-spacing: 1px;
  }
  .accent-rail {
    position: absolute;
    left: 800px;
    top: 0;
    width: 60px;
    height: 580px;
  }
</style>
</head>
<body>
  <main class="canvas">
    <section class="business-card">
      <div class="identity">
        <h1 class="identity__name">Lana Frost</h1>
        <p class="identity__services">Events • Entertainment • Promotions</p>
        <p class="identity__phone">0491726580</p>
      </div>
      <svg class="accent-rail" viewBox="0 0 60 580" aria-hidden="true">
        <line x1="30" y1="0" x2="30" y2="262" stroke="var(--gold)" stroke-width="4"/>
        <circle cx="30" cy="288" r="18" fill="none" stroke="var(--gold)" stroke-width="2"/>
        <circle cx="30" cy="334" r="18" fill="none" stroke="var(--gold)" stroke-width="2"/>
        <circle cx="30" cy="380" r="18" fill="none" stroke="var(--gold)" stroke-width="2"/>
        <line x1="30" y1="406" x2="30" y2="460" stroke="var(--gold)" stroke-width="4"/>
      </svg>
    </section>
  </main>
</body>
</html>
```